Criação de Kit com 5 Layouts de Post para Redes Sociais (Facebook, Instagram e etc) para Consultoria de Negócios
" EVENTO DE DOIS DIAS COM VÁRIOS PALESTRANTES, TRAZENDO CONHECIMENTO EM VARIAS ÁREAS PARA AS MULHERES EMPREENDEDORAS. UM EVENTO DE IMERSSAO DE 19 HORAS. "

```html
<!DOCTYPE html>
<html lang="pt-BR">
<head>
<meta charset="UTF-8">
<title>AVEM – Post</title>
<link rel="stylesheet" href="https://fonts.googleapis.com/css2?family=Cinzel:wght@400;700&display=swap">
<style>
  :root {
    --gold: #c9a45c;
    --gold-light: #e6cf94;
    --white: #ffffff;
    --ink: #0e0d0c;
    --photo-dark: #4a4541;
    --photo-mid: #8d857e;
    --photo-light: #d6cec6;
  }
  * { margin: 0; padding: 0; box-sizing: border-box; }
  html, body { width: 1200px; height: 1200px; overflow: hidden; background: var(--ink); }
  .post {
    position: relative;
    width: 1200px;
    height: 1200px;
    overflow: hidden;
    font-family: "Cinzel", serif;
    color: var(--white);
  }
  .post__photo {
    position: absolute;
    inset: 0;
    background:
      radial-gradient(ellipse at 70% 55%, rgba(230,222,214,0.55) 0%, rgba(230,222,214,0) 55%),
      linear-gradient(180deg, rgba(40,36,33,0.55) 0%, rgba(40,36,33,0) 30%, rgba(40,36,33,0) 65%, rgba(30,27,25,0.6) 100%),
      linear-gradient(110deg, var(--photo-light) 0%, var(--photo-mid) 45%, var(--photo-light) 75%, var(--photo-dark) 100%);
  }
  .brand {
    position: absolute;
    left: 72px;
    top: 74px;
    display: flex;
    align-items: center;
    gap: 24px;
  }
  .brand__mark {
    width: 140px;
    height: 140px;
    border-radius: 50%;
    border: 3px solid var(--gold);
  }
  .brand__name {
    font-size: 92px;
    font-weight: 400;
    letter-spacing: 4px;
    line-height: 1;
    color: var(--white);
  }
  .brand__tagline {
    position: absolute;
    left: 236px;
    top: 182px;
    font-size: 15px;
    line-height: 1.5;
    letter-spacing: 1px;
    text-transform: uppercase;
    color: var(--white);
  }
  .frame-lines { position: absolute; inset: 0; }
  .headline {
    position: absolute;
    left: 72px;
    top: 872px;
    width: 530px;
    font-size: 31px;
    font-weight: 700;
    line-height: 57px;
    text-align: justify;
    text-align-last: justify;
    color: var(--white);
    text-shadow: 0 2px 6px rgba(0,0,0,0.35);
  }
  .footer-band { position: absolute; left: 0; bottom: 0; width: 1200px; height: 110px; }
  .site {
    position: absolute;
    right: 30px;
    bottom: 18px;
    font-size: 38px;
    font-weight: 400;
    letter-spacing: 1px;
    color: var(--white);
  }
</style>
</head>
<body>
<main class="post">
  <div class="post__photo" role="img" aria-label="Fotografia de uma mulher digitando em um notebook sobre uma mesa de madeira, em tons suaves de cinza e bege"></div>

  <svg class="frame-lines" width="1200" height="1200" viewBox="0 0 1200 1200" aria-hidden="true">
    <line x1="516" y1="149" x2="1130" y2="149" stroke="var(--gold)" stroke-width="4"/>
    <line x1="1027" y1="43" x2="1027" y2="650" stroke="var(--gold)" stroke-width="4"/>
  </svg>

  <div class="brand">
    <div class="brand__mark"></div>
    <div class="brand__name">AVEM</div>
  </div>
  <p class="brand__tagline">Encontro de Avanço &amp;<br>Visão Empreendedora</p>

  <p class="headline">Lorem ipsum dolor sit amet, consectetuer adipiscing elit, sed diam nonummy nibh euismod tincidunt ut laoreet</p>

  <svg class="footer-band" width="1200" height="110" viewBox="0 0 1200 110" aria-hidden="true">
    <path d="M0 60 Q600 0 1200 18 L1200 110 L0 110 Z" fill="var(--ink)"/>
    <path d="M0 60 Q600 0 1200 18" fill="none" stroke="var(--gold-light)" stroke-width="5"/>
  </svg>
  <p class="site">WWW.SEUSITE.COM.BR</p>
</main>
</body>
</html>
```